QZmortgage303.com needs a website.

I'm looking for a website that offeres education and courses about the QZ home loan. This will teach people what they need to know about using the QZ loan. I need a website design that will allow the use of video, have sections to educate about the myths out there, use blue and red which are patriotic colors.

```html
<!DOCTYPE html>
<html lang="en">
<head>
<meta charset="utf-8">
<title>QZmortgage303.com – Learn Everything About QZ Home Loan</title>
<link href="https://fonts.googleapis.com/css2?family=Poppins:wght@400;500;600&family=Roboto:wght@400;500&display=swap" rel="stylesheet">
<style>
:root{
  --blue:#1a5fd6;
  --navy:#0d1f5c;
  --ink:#0f1d4a;
  --text:#5b6275;
  --muted:#8a90a0;
  --soft:#f3f4f7;
  --line:#e6e8ee;
  --white:#fff;
  --red:#d4252d;
  --yellow:#f3c21a;
}
*{margin:0;padding:0;box-sizing:border-box}
html,body{width:1200px;height:4608px;overflow:hidden}
body{position:relative;background:var(--white);font-family:'Roboto',sans-serif;color:var(--text);font-size:12px}
.abs{position:absolute}
h1,h2,h3,h4{font-family:'Poppins',sans-serif;color:var(--ink);font-weight:500}
.label{font-size:11px;color:var(--blue);font-weight:500}
.btn{position:absolute;background:var(--blue);color:#fff;font-size:10px;font-weight:500;display:flex;align-items:center;justify-content:center;gap:8px;letter-spacing:.3px}
.btn svg{width:12px;height:8px}
.ph{position:absolute}
/* top bar */
.topbar{position:absolute;left:0;top:0;width:1200px;height:32px;background:var(--navy)}
.topbar span{position:absolute;top:10px;font-size:9.5px;color:#fff}
.nav{position:absolute;left:0;top:32px;width:1200px;height:58px;background:#fff;border-bottom:1px solid var(--line)}
.nav a{position:absolute;top:22px;font-size:11px;color:var(--ink);text-decoration:none}
.logo{position:absolute;left:125px;top:0;width:131px;height:80px;background:var(--blue);border-radius:0 0 6px 6px;display:flex;align-items:flex-end;justify-content:center;padding-bottom:10px;color:#fff;font-family:'Roboto',sans-serif;font-size:10.5px;font-weight:500;z-index:2}
.social{position:absolute;top:11px;width:9px;height:9px;border-radius:50%;background:#fff}
/* features band */
.band{position:absolute;left:0;top:638px;width:1200px;height:160px;background:var(--navy)}
.feat{position:absolute;top:48px;width:230px}
.feat .ic{position:absolute;left:0;top:0;width:56px;height:56px;border-radius:50%}
.feat h4{position:absolute;left:75px;top:6px;color:#fff;font-size:13px;white-space:nowrap}
.feat p{position:absolute;left:75px;top:28px;color:#c8cfe6;font-size:9.5px;line-height:16px;width:160px}
/* courses */
.card{position:absolute;width:231px;height:267px;background:#fff;box-shadow:0 2px 8px rgba(15,29,74,.06)}
.card .img{position:absolute;left:0;top:0;width:231px;height:143px}
.card h4{position:absolute;left:26px;top:178px;font-size:13px}
.card .rule{position:absolute;left:26px;right:26px;top:212px;height:1px;background:var(--line)}
.card .who{position:absolute;left:26px;top:228px;display:flex;align-items:center;gap:10px;font-size:9.5px;color:var(--ink)}
.card .who i{width:22px;height:22px;border-radius:50%;background:var(--blue);color:#fff;font-style:normal;font-size:8px;display:flex;align-items:center;justify-content:center}
.card .enroll{position:absolute;right:24px;top:222px;width:80px;height:30px;background:var(--blue);color:#fff;font-size:10px;font-weight:500;display:flex;align-items:center;justify-content:center}
.check{display:flex;align-items:flex-start;gap:12px;font-size:11px;color:var(--ink);font-weight:500;line-height:17px}
.check svg{flex:none;width:16px;height:16px}
.stat{position:absolute;width:170px}
.stat .ic{position:absolute;left:0;top:0;width:56px;height:56px;border-radius:50%;background:var(--soft)}
.stat b{position:absolute;left:68px;top:2px;font-family:'Poppins',sans-serif;font-size:24px;font-weight:500;color:var(--ink)}
.stat span{position:absolute;left:68px;top:38px;font-size:9.5px;color:var(--ink)}
.event{position:absolute;left:610px;width:356px;height:136px;background:#fff}
.event .img{position:absolute;left:12px;top:12px;width:126px;height:112px}
.event .date{position:absolute;left:86px;top:95px;width:92px;height:20px;background:var(--blue);color:#fff;font-size:8px;display:flex;align-items:center;justify-content:center}
.event h4{position:absolute;left:156px;top:22px;font-size:14px;line-height:21px}
.event .place{position:absolute;left:200px;top:92px;font-size:8.5px;color:var(--text)}
.foot h4{color:#fff;font-size:13px;position:absolute}
.foot a,.foot p{position:absolute;color:#fff;font-size:9.5px;text-decoration:none;line-height:16px}
</style>
</head>
<body>

<!-- Header -->
<div class="topbar">
  <span style="left:306px">⚲ Address : 41 Elm Row Denver, USA</span>
  <span style="left:489px;color:#7f8ab8">|</span>
  <span style="left:510px">◷ Working : Monday - Friday, 9:Am - 5:Pm</span>
  <span style="left:874px">⚇ Login/ Register</span>
  <span style="left:976px;color:#7f8ab8">|</span>
  <i class="social" style="left:998px"></i><i class="social" style="left:1020px"></i><i class="social" style="left:1042px"></i><i class="social" style="left:1064px"></i>
</div>
<div class="logo">QZmortgage303.com</div>
<nav class="nav">
  <a style="left:412px;color:var(--blue)">Home</a>
  <a style="left:471px">About Us</a>
  <a style="left:547px">Courses</a>
  <a style="left:618px">Video Library</a>
  <a style="left:717px">Blog</a>
  <a style="left:769px">Contact</a>
  <svg class="abs" style="left:983px;top:22px" width="14" height="14" viewBox="0 0 14 14"><circle cx="6" cy="6" r="4.5" fill="none" stroke="#0f1d4a" stroke-width="1.5"/><path d="M9.5 9.5 13 13" stroke="#0f1d4a" stroke-width="1.5"/></svg>
  <svg class="abs" style="left:1017px;top:21px" width="14" height="15" viewBox="0 0 14 15"><rect x="1.5" y="4.5" width="11" height="9" fill="none" stroke="#0f1d4a" stroke-width="1.4"/><path d="M4.5 4.5V3a2.5 2.5 0 0 1 5 0v1.5" fill="none" stroke="#0f1d4a" stroke-width="1.4"/></svg>
  <span class="abs" style="left:1027px;top:17px;width:10px;height:10px;border-radius:50%;background:var(--blue);color:#fff;font-size:7px;text-align:center;line-height:10px">0</span>
  <svg class="abs" style="left:1059px;top:23px" width="18" height="12" viewBox="0 0 18 12"><path d="M0 1h18M4 6h14M8 11h10" stroke="#1a5fd6" stroke-width="1.6"/></svg>
</nav>

<!-- Hero -->
<section class="hero">
  <div class="label abs" style="left:234px;top:196px">We're QZ Home Loan Specialists</div>
  <h1 class="abs" style="left:233px;top:222px;font-size:52px;line-height:57px;font-weight:500">Learn Everything<br>About QZ Home<br>Loan</h1>
  <p class="abs" style="left:234px;top:410px;width:350px;font-size:10.5px;line-height:20px">We're Not Just QZ Home Loan Specialists—We Are Educators And Community Leaders. We're Committed To Educating, Supporting And Serving Military Families.</p>
  <div class="btn" style="left:234px;top:500px;width:135px;height:37px">LEARN MORE <svg viewBox="0 0 12 8"><path d="M0 4h11M8 1l3 3-3 3" fill="none" stroke="#fff" stroke-width="1.3"/></svg></div>
  <div class="abs" style="left:668px;top:214px;width:235px;height:283px;border:2px solid var(--blue)"></div>
  <div class="ph" role="img" aria-label="Soldier in uniform reviewing home loan papers with small model houses" style="left:665px;top:211px;width:235px;height:283px;background:linear-gradient(135deg,#8a8478,#c9c1b2 55%,#6d6a5f)"></div>
  <div class="ph" role="img" aria-label="Loan application form close-up" style="left:919px;top:168px;width:154px;height:79px;background:linear-gradient(135deg,#e9e6e0,#bfb9ae)"></div>
  <div class="ph" role="img" aria-label="Military family greeting a returning soldier" style="left:919px;top:261px;width:154px;height:158px;background:linear-gradient(135deg,#5b6b7e,#a2a9b0 60%,#4c5560)"></div>
  <div class="ph" role="img" aria-label="Hands holding a small house painted with the national flag" style="left:919px;top:433px;width:154px;height:104px;background:linear-gradient(135deg,#3f4a38,#b6404a 55%,#3a4c7a)"></div>
</section>

<!-- Features -->
<section class="band">
  <div class="feat" style="left:234px"><i class="ic" style="background:#2bb5a8"></i><h4>Professional Mentor</h4><p>Pellentesque Ante, Non Eleifend Justo Bibendum A.</p></div>
  <div class="feat" style="left:485px"><i class="ic" style="background:#6a5be0"></i><h4>Lifetime Access</h4><p>Pellentesque Ante, Non Eleifend Justo Bibendum A.</p></div>
  <div class="feat" style="left:735px"><i class="ic" style="background:#2ea99a"></i><h4>Ofline And Online</h4><p>Pellentesque Ante, Non Eleifend Justo Bibendum A.</p></div>
</section>

<!-- About -->
<section class="about">
  <div class="ph" role="img" aria-label="Service member in dress uniform and cap outdoors" style="left:234px;top:875px;width:261px;height:164px;background:linear-gradient(135deg,#8fb07a,#dfe0d8 60%,#b6a27a)"></div>
  <div class="ph" role="img" aria-label="Rows of small flags on a lawn at sunset" style="left:191px;top:1007px;width:199px;height:231px;background:linear-gradient(180deg,#6f7fae,#b7574f 55%,#4d7a2e);box-shadow:-6px -6px 0 #0d1f5c"></div>
  <div class="ph" role="img" aria-label="Service member working on a laptop at home" style="left:424px;top:1070px;width:141px;height:143px;background:linear-gradient(135deg,#d8d2c8,#8b7d68)"></div>
  <div class="label abs" style="left:610px;top:892px">About Us</div>
  <h2 class="abs" style="left:609px;top:914px;font-size:30px;line-height:41px">Educating About<br>QZ Home Loan</h2>
  <p class="abs" style="left:610px;top:1013px;width:310px;font-size:9.5px;line-height:16px">Pellentesque Non Aliquet Sem. Aliquam Facilisis Nec Velit Vitae Commodo. Orci Varius Natoque Penatibus Et Magnis Dis Parturient Montes, Nascetur Ridiculus Mus.</p>
  <div class="check abs" style="left:610px;top:1096px;font-size:10.5px"><svg viewBox="0 0 16 16"><circle cx="8" cy="8" r="8" fill="#eef1f8"/><path d="M4.5 8.2 7 10.5l4.5-5" fill="none" stroke="#1a5fd6" stroke-width="1.5"/></svg>Unique Support System</div>
  <div class="check abs" style="left:610px;top:1133px;font-size:10.5px"><svg viewBox="0 0 16 16"><circle cx="8" cy="8" r="8" fill="#eef1f8"/><path d="M4.5 8.2 7 10.5l4.5-5" fill="none" stroke="#1a5fd6" stroke-width="1.5"/></svg>Organization Of Education</div>
  <div class="ph" role="img" aria-label="Portrait of the founder" style="left:841px;top:1093px;width:48px;height:48px;border-radius:50%;background:linear-gradient(135deg,#e6c9c0,#9a6f6a)"></div>
  <div class="abs" style="left:841px;top:1153px;font-size:12px;font-weight:500;color:var(--ink);font-family:'Poppins',sans-serif">Marcus Hale</div>
  <div class="abs" style="left:841px;top:1175px;font-size:9px">Founder Of CEO</div>
  <div class="btn" style="left:610px;top:1185px;width:133px;height:37px">LEARN MORE <svg viewBox="0 0 12 8"><path d="M0 4h11M8 1l3 3-3 3" fill="none" stroke="#fff" stroke-width="1.3"/></svg></div>
</section>

<!-- Courses -->
<section class="abs" style="left:0;top:1315px;width:1200px;height:805px;background:var(--soft)">
  <div class="label abs" style="left:0;width:1200px;text-align:center;top:74px">What We Offer!</div>
  <h2 class="abs" style="left:0;width:1200px;text-align:center;top:104px;font-size:30px">Our Unique Courses</h2>
</section>
<div class="card" style="left:234px;top:1490px"><div class="img" role="img" aria-label="Man studying at a desk with a laptop" style="background:linear-gradient(135deg,#d9d4cc,#6d6258)"></div><h4>Loan Basics</h4><div class="rule"></div><div class="who" style="top:224px"><i>0</i>Developer</div></div>
<div class="card" style="left:485px;top:1490px"><div class="img" role="img" aria-label="Student at a desktop computer in the evening" style="background:linear-gradient(135deg,#4a4036,#c6a46a)"></div><h4>Eligibility Criteria</h4><div class="rule"></div><div class="who"><i>0</i>Developer</div><div class="enroll">Enroll Course</div></div>
<div class="card" style="left:735px;top:1490px"><div class="img" role="img" aria-label="Couple relaxing on a sofa with a laptop" style="background:linear-gradient(135deg,#e7e4df,#9c9a96)"></div><h4>QZ Appraisals / LAPP</h4><div class="rule"></div><div class="who"><i>0</i>Developer</div><div class="enroll">Enroll Course</div></div>
<div class="card" style="left:234px;top:1778px"><div class="img" role="img" aria-label="Teacher at a chalkboard with a laptop" style="background:linear-gradient(135deg,#2f3a30,#a2835e)"></div><h4>Credit Underwriting</h4><div class="rule"></div><div class="who"><i>0</i>Developer</div><div class="enroll">Enroll Course</div></div>
<div class="card" style="left:485px;top:1778px"><div class="img" role="img" aria-label="Stack of colourful document folders" style="background:linear-gradient(135deg,#7aa6d6,#e7d6c0 60%,#c89a5a)"></div><h4>Closing And Submission</h4><div class="rule"></div><div class="who" style="top:224px"><i>0</i>Developer</div></div>
<div class="card" style="left:735px;top:1778px"><div class="img" role="img" aria-label="Service member and child using a laptop" style="background:linear-gradient(135deg,#eeebe5,#8a8466)"></div><h4>Loan Processing Steps</h4><div class="rule"></div><div class="who" style="top:224px"><i>0</i>Developer</div></div>

<!-- Eligibility / video -->
<section>
  <div class="abs" style="left:234px;top:2236px;width:419px;height:439px;background:var(--soft)"></div>
  <div class="ph" role="img" aria-label="Soldier father lying on the floor with his baby" style="left:610px;top:2195px;width:356px;height:480px;background:linear-gradient(160deg,#3a3a3a,#b9a997 40%,#6b6e5c)"></div>
  <svg class="abs" style="left:634px;top:2216px" width="80" height="80" viewBox="0 0 80 80"><circle cx="40" cy="40" r="40" fill="#1a5fd6"/><path d="M33 28v24l19-12z" fill="#fff"/></svg>
  <div class="label abs" style="left:286px;top:2287px">Learn Wo Is</div>
  <h2 class="abs" style="left:286px;top:2309px;font-size:30px;line-height:41px">Eligible For A 0%<br>Down QZ Home Loan?</h2>
  <p class="abs" style="left:286px;top:2411px;width:310px;font-size:9.5px;line-height:16px">Pellentesque Non Aliquet Sem. Aliquam Facilisis Nec Velit Vitae Commodo. Orci Varius Natoque Penatibus Et Magnis Dis Parturient Montes, Nascetur Ridiculus Mus.</p>
  <div class="check abs" style="left:286px;top:2487px;width:290px;font-size:10px"><svg viewBox="0 0 16 16"><circle cx="8" cy="8" r="8" fill="#22b07d"/><path d="M4.5 8.2 7 10.5l4.5-5" fill="none" stroke="#fff" stroke-width="1.5"/></svg>High High-Quality Student-Tutor Interactions Education System</div>
  <div class="check abs" style="left:286px;top:2539px;font-size:10px"><svg viewBox="0 0 16 16"><circle cx="8" cy="8" r="8" fill="#1a5fd6"/><path d="M4.5 8.2 7 10.5l4.5-5" fill="none" stroke="#fff" stroke-width="1.5"/></svg>Online Learning Offers Convenience And Flexibility</div>
  <div class="btn" style="left:286px;top:2590px;width:138px;height:37px">JOIN WITH US <svg viewBox="0 0 12 8"><path d="M0 4h11M8 1l3 3-3 3" fill="none" stroke="#fff" stroke-width="1.3"/></svg></div>
</section>

<!-- Achievement -->
<section>
  <div class="abs" style="left:216px;top:2762px;width:321px;height:321px;border-radius:50%;background:var(--soft)"></div>
  <div class="ph" role="img" aria-label="Smiling man in a blazer holding a laptop" style="left:222px;top:2746px;width:300px;height:392px;border-radius:140px 140px 0 0;background:linear-gradient(180deg,#6b4a34,#2d2f38 45%,#8d8f96)"></div>
  <div class="label abs" style="left:610px;top:2753px">Achievement</div>
  <h2 class="abs" style="left:609px;top:2775px;font-size:30px;line-height:41px">Our Only Concern Is<br>Educating You</h2>
  <p class="abs" style="left:610px;top:2875px;width:350px;font-size:9.5px;line-height:16px">Aliquam Sagittis Tortor Felis, Id Auctor Dui Tempus Sit Amet. Integer Viverra Mauris Nec Auctor Sagittis.</p>
  <div class="stat" style="left:610px;top:2941px"><i class="ic"></i><b>353k</b><span>Happy Students</span></div>
  <div class="stat" style="left:788px;top:2941px"><i class="ic"></i><b>129+</b><span>Expert Instructors</span></div>
  <div class="stat" style="left:610px;top:3023px"><i class="ic"></i><b>15k+</b><span>Popular Courses</span></div>
  <div class="stat" style="left:788px;top:3023px"><i class="ic"></i><b>152k</b><span>Mobile Apps Users</span></div>
</section>

<!-- Events -->
<section class="abs" style="left:0;top:3138px;width:1200px;height:444px;background:var(--navy)"></section>
<div class="label abs" style="left:234px;top:3213px;color:#4f8bf0">Our Events</div>
<h2 class="abs" style="left:234px;top:3235px;font-size:30px;line-height:41px;color:#fff">We Organize<br>Yearly Events<br>And Programs</h2>
<p class="abs" style="left:234px;top:3378px;width:290px;font-size:9.5px;line-height:16px;color:#d4d9ea">Aliquam Sagittis Tortor Felis, Id Auctor Dui Tempus Sit Amet. Integer Viverra Mauris Nec Auctor Sagittis.</p>
<div class="btn" style="left:234px;top:3445px;width:122px;height:36px">VIEWS ALL <svg viewBox="0 0 12 8"><path d="M0 4h11M8 1l3 3-3 3" fill="none" stroke="#fff" stroke-width="1.3"/></svg></div>
<div class="event" style="top:3213px"><div class="img" role="img" aria-label="Two students smiling at a laptop" style="background:linear-gradient(135deg,#e2ddd5,#7d6a5c)"></div><div class="date">▦ 31 March, 2023</div><h4>Your Understanding<br>Is Our Success</h4><div class="place">▥ 41 Elm Row Leeds, UK</div></div>
<div class="event" style="top:3371px"><div class="img" role="img" aria-label="Group of students studying together" style="background:linear-gradient(135deg,#ebe6df,#8a6c66)"></div><div class="date">▦ 31 March, 2023</div><h4>Your Understanding<br>Is Our Success</h4><div class="place">▥ 41 Elm Row Leeds, UK</div></div>

<!-- Testimonial -->
<section>
  <div class="label abs" style="left:234px;top:3656px">Testimonial</div>
  <h2 class="abs" style="left:234px;top:3678px;font-size:30px;line-height:41px">What Community<br>Says About Us</h2>
  <div class="abs" style="left:234px;top:3782px;font-size:10.5px;color:var(--ink)">12.56k+ Students Join With Studyline</div>
  <svg class="abs" style="left:234px;top:3860px" width="82" height="36" viewBox="0 0 82 36"><circle cx="18" cy="18" r="17" fill="none" stroke="#1a5fd6" stroke-width="1.3"/><path d="M24 18H12m4-4-4 4 4 4" fill="none" stroke="#1a5fd6" stroke-width="1.3"/><circle cx="64" cy="18" r="17" fill="none" stroke="#1a5fd6" stroke-width="1.3"/><path d="M58 18h12m-4-4 4 4-4 4" fill="none" stroke="#1a5fd6" stroke-width="1.3"/></svg>
  <div class="abs" style="left:553px;top:3696px;width:261px;height:197px;background:var(--soft)"></div>
  <div class="ph" role="img" aria-label="Cheerful man in a red shirt celebrating" style="left:735px;top:3657px;width:231px;height:218px;background:linear-gradient(135deg,#3fb1d3,#c9a58a 50%,#c4272f)"></div>
  <svg class="abs" style="left:554px;top:3657px" width="32" height="32" viewBox="0 0 32 32"><circle cx="16" cy="16" r="16" fill="#5a6385"/><path d="M16 10v12M10 16h12" stroke="#fff" stroke-width="1.6"/></svg>
  <div class="abs" style="left:583px;top:3748px;font-family:'Poppins',sans-serif;font-size:13px;color:var(--ink);font-weight:500">Marcus Hale</div>
  <div class="abs" style="left:583px;top:3770px;font-size:9px;color:var(--blue)">UI-Designer</div>
  <p class="abs" style="left:583px;top:3796px;width:205px;font-size:9.5px;line-height:16px">Aliquam Sagittis Tortor Felis, Id Auctor Dui Tempus Sit Amet. Integer Viverra Mauris Nec Auctor Sagittis. Morbi Euismod Lacus Et Enim Commodo Imperdiet.</p>
</section>

<!-- CTA + Footer -->
<section class="abs" style="left:0;top:4127px;width:1200px;height:481px;background:var(--navy)"></section>
<div class="abs" style="left:234px;top:4014px;width:732px;height:249px;background:linear-gradient(135deg,#1a5fd6,#2f79e6)"></div>
<h2 class="abs" style="left:278px;top:4064px;font-size:30px;line-height:41px;color:#fff">Join The Best Learning Platform<br>For QZ Home Loan Today</h2>
<div class="btn" style="left:278px;top:4176px;width:139px;height:36px;background:#e9edf7;color:var(--ink)">JOIN WITH US <svg viewBox="0 0 12 8"><path d="M0 4h11M8 1l3 3-3 3" fill="none" stroke="#0f1d4a" stroke-width="1.3"/></svg></div>
<svg class="abs" style="left:840px;top:4100px" width="82" height="82" viewBox="0 0 82 82"><circle cx="41" cy="41" r="41" fill="#f3c21a"/><circle cx="41" cy="41" r="29" fill="none" stroke="#0f1d4a" stroke-width="1.5"/><path d="M35 31v20l16-10z" fill="#0f1d4a"/></svg>

<footer class="foot">
  <h4 style="left:234px;top:4314px">Get Started</h4>
  <p style="left:234px;top:4346px;width:195px">Integer Gravida Posuere Lacus Et Suscipit. Pellentesque Sed Ipsum Sollicitudin, Fermentum Nibh Elementum, Dignissim Leo. In Hac Habitasse Platea Dictumst.</p>
  <div class="abs" style="left:234px;top:4435px;width:132px;height:34px;background:#fff;font-size:9px;color:var(--muted);padding:12px 16px">Email Address</div>
  <div class="abs" style="left:366px;top:4435px;width:37px;height:34px;background:var(--blue)"><svg style="position:absolute;left:12px;top:11px" width="13" height="12" viewBox="0 0 13 12"><path d="M13 0 0 6l4 1.5L13 0 5 8v4l2.5-3L10 11z" fill="#fff"/></svg></div>

  <h4 style="left:485px;top:4314px">Our Course</h4>
  <a style="left:485px;top:4346px">Loan Basics</a>
  <a style="left:485px;top:4373px">Eligibility Criteria</a>
  <a style="left:485px;top:4400px">QZ Appraisals / LAPP</a>
  <a style="left:485px;top:4427px">Credit Underwriting</a>
  <a style="left:485px;top:4454px">Loan Processing Steps</a>

  <h4 style="left:646px;top:4314px">Company</h4>
  <a style="left:646px;top:4346px">About Us</a>
  <a style="left:646px;top:4373px">Become An Instructor</a>
  <a style="left:646px;top:4400px">Student Registration</a>
  <a style="left:646px;top:4427px">FAQs</a>
  <a style="left:646px;top:4454px">Contact Us</a>

  <h4 style="left:796px;top:4314px">Infomation</h4>
  <p style="left:820px;top:4346px">(+1) 555 010 234</p>
  <p style="left:820px;top:4373px">info@QZmortgage303.com</p>
  <p style="left:820px;top:4400px">18 Birch Way Denver,<br>United States</p>
  <i class="abs" style="left:797px;top:4348px;width:13px;height:13px;border-radius:50%;border:1.3px solid #4f8bf0"></i>
  <i class="abs" style="left:797px;top:4375px;width:14px;height:11px;border:1.3px solid #4f8bf0"></i>
  <i class="abs" style="left:799px;top:4402px;width:10px;height:13px;border-radius:50% 50% 50% 0;border:1.3px solid #4f8bf0"></i>
  <i class="abs" style="left:797px;top:4452px;width:20px;height:20px;border-radius:50%;background:#27386f"></i>
  <i class="abs" style="left:829px;top:4452px;width:20px;height:20px;border-radius:50%;background:#27386f"></i>
  <i class="abs" style="left:861px;top:4452px;width:20px;height:20px;border-radius:50%;background:#27386f"></i>
  <i class="abs" style="left:893px;top:4452px;width:20px;height:20px;border-radius:50%;background:#27386f"></i>

  <div class="abs" style="left:234px;top:4548px;width:732px;height:1px;background:#26367a"></div>
  <p style="left:234px;top:4574px">Copyright © 2023 QZ Mortgage 303. All Rights Reserved.</p>
  <p style="left:820px;top:4574px">Support &nbsp;&nbsp;| &nbsp;&nbsp;Privacy &nbsp;&nbsp;| &nbsp;&nbsp;Policy</p>
  <div class="abs" style="left:1160px;top:4525px;width:28px;height:28px;background:var(--blue)"><svg style="position:absolute;left:9px;top:10px" width="10" height="7" viewBox="0 0 10 7"><path d="M1 6l4-4 4 4" fill="none" stroke="#fff" stroke-width="1.5"/></svg></div>
</footer>

</body>
</html>
```